starlitmanesandtails pet therapy animals

I would like a business card to genarate posative emotions within people. My program has been running in a retirement village for over 5 years I work with residents and family members. My dogs work in palative care and are a great support to family members at the end stage. I also support the families and friends at furnerals when needed to dogs are always with me. Starlitmanes started with the death of my first therapy dog Milo there was such an out cry of grief within the town and retirement village that he had his own furneral The hooves came into it when I was donated a beautiful Miniature horse for the pet therapy program with great results. I now need something very special as a business card. Eg Angelwings my dogs are King Charles Cavaliers so with what I have described can you create something beautiful to acknowledge to work I do and promote it more.

Reason: The reason I have extended the deadline to give other designers a chance to look at the job. So far I have 3 designs. I am hoping to get a few more.

Industry/Entity Type

Town

Contact Information for Business Card

Starlitmanesandtails pet therapy animals
Rosalind Varga
E-mail starlitmanesandtails@quellnet.com
Mobile 0417650382
Pet therapy animals give unconditional love to the aged and disabled.

Font styles to use
Decorative

Colors

Designer to choose colors to be used in the design.

Requirements
Nice to have
• angelwings a King Charles Cavalier tan and white with angel wings and a horse with angel wings

```html
<!DOCTYPE html>
<html lang="en">
<head>
<meta charset="utf-8">
<title>Starlitmanesandtails – Business Card</title>
<link href="https://fonts.googleapis.com/css2?family=Cinzel:wght@400;700&family=Arimo:wght@400;700&display=swap" rel="stylesheet">
<style>
  :root {
    --backdrop: #e9e6e2;
    --front-light: #e6f5fd;
    --front-mid: #bfe5f8;
    --front-edge: #9fd6f2;
    --brand-blue: #1f4c86;
    --art-white: #ffffff;
    --art-tint: #d9eefb;
    --art-edge: #8fc0e6;
    --back-blue: #1d4a85;
    --rule-blue: #5b8fc8;
    --soft-text: #cfe3f7;
    --white: #ffffff;
    --icon-blue: #3aa6e6;
  }
  * { margin: 0; padding: 0; box-sizing: border-box; }
  html, body {
    width: 1200px; height: 581px; overflow: hidden;
    background: var(--backdrop);
  }
  .card {
    position: absolute; left: 127px; top: 145px;
    width: 946px; height: 291px;
    display: flex;
    box-shadow: 0 4px 12px rgba(0,0,0,0.25);
  }
  .card-front {
    position: relative; width: 473px; height: 100%;
    background: radial-gradient(ellipse at 48% 42%, var(--front-light) 0%, var(--front-mid) 55%, var(--front-edge) 100%);
  }
  .mascot-art {
    position: absolute; left: 152px; top: 74px;
    width: 168px; height: 114px;
    border-radius: 46% 46% 38% 38%;
    background: radial-gradient(ellipse at 50% 50%, var(--art-white) 0%, var(--art-tint) 60%, var(--art-edge) 100%);
    box-shadow: 0 8px 10px -6px rgba(31,76,134,0.35);
  }
  .brand-name {
    position: absolute; left: 0; width: 473px; top: 205px;
    text-align: center;
    font-family: 'Cinzel', serif; font-weight: 400;
    font-size: 27px; letter-spacing: 0.5px;
    color: var(--brand-blue);
  }
  .brand-tagline {
    position: absolute; left: 63px; width: 318px; top: 236px;
    display: flex; align-items: center; gap: 6px;
    font-family: 'Arimo', sans-serif; font-size: 11px; font-weight: 700;
    color: var(--brand-blue); white-space: nowrap;
  }
  .brand-tagline::before, .brand-tagline::after {
    content: ""; flex: 1; height: 1px; background: var(--brand-blue);
  }
  .card-back {
    position: relative; width: 473px; height: 100%;
    background: var(--back-blue);
    color: var(--white);
  }
  .holder-name {
    position: absolute; left: 0; width: 473px; top: 130px;
    text-align: center;
    font-family: 'Cinzel', serif; font-weight: 700;
    font-size: 24px; letter-spacing: 1px;
  }
  .mission {
    position: absolute; left: 110px; width: 252px; top: 194px;
    border-top: 1px solid var(--rule-blue);
    border-bottom: 1px solid var(--rule-blue);
    padding: 2px 0 3px;
    text-align: center;
    font-family: 'Arimo', sans-serif; font-size: 12px; line-height: 14px;
    color: var(--soft-text);
  }
  .contact-line {
    position: absolute; left: 0; width: 473px; top: 233px;
    display: flex; justify-content: center; align-items: center; gap: 5px;
    font-family: 'Arimo', sans-serif; font-weight: 700; font-size: 14px;
    white-space: nowrap;
  }
  .contact-line .phone-icon { margin-left: 6px; }
  .contact-line svg { display: block; }
</style>
</head>
<body>
  <div class="card">
    <section class="card-front">
      <div class="mascot-art" role="img" aria-label="Illustration of a therapy dog with angel wings and a halo"></div>
      <div class="brand-name">Starlitmanesandtails</div>
      <div class="brand-tagline">PET THERAPY ANIMALS</div>
    </section>
    <section class="card-back">
      <h1 class="holder-name">Rosalind Varga</h1>
      <p class="mission">Pet therapy animals give unconditional love<br>to the aged and disabled.</p>
      <p class="contact-line">
        <svg class="mail-icon" width="14" height="12" viewBox="0 0 14 12" aria-hidden="true">
          <rect x="0" y="0" width="14" height="12" rx="3" fill="var(--icon-blue)"/>
          <rect x="3" y="3.5" width="8" height="5" fill="none" stroke="var(--back-blue)" stroke-width="1"/>
          <path d="M3 3.5 L7 6.5 L11 3.5" fill="none" stroke="var(--back-blue)" stroke-width="1"/>
        </svg>
        <span>starlitmanesandtails@quellnet.com</span>
        <svg class="phone-icon" width="12" height="14" viewBox="0 0 12 14" aria-hidden="true">
          <rect x="0" y="0" width="12" height="14" rx="3" fill="var(--icon-blue)"/>
          <path d="M5 3 C3 4 3 10 5 11 L6.5 9.5 L5.5 8 C5 7 5 7 5.5 6 L6.5 4.5 Z" fill="var(--back-blue)"/>
        </svg>
        <span>0417650382</span>
      </p>
    </section>
  </div>
</body>
</html>
```